Invitation for Executives

We need an eye-catching design for a direct mail invitation to executives. The invitation will be printed on A3 paper, so the image needs to be very crisp. The invitation details are attached in a word document. Note that the location details etc will be finalised at the end of the contest, so the winner will need to update the final file

Calloway Institute has a special red colour that it uses for all marketing materials - the colour description is Pantone 1807 CMYK C:0 M:91 Y:94 K:30 RGB R:177 G:44 B:27 . Go to the website listed on the invitation details to have a look at the Calloway styles used on the website.
The Calloway logo is CALLOWAY in truesdell font, in the special red colour (or white if that red is the background)

Note - we have decided not to feature the Calloway logo - it will be enough to have the sponsorship byline and link to website, and let the speaker's credentials speak for themselves

Target Market(s)

senior executives (CEO's, CIOs, CFOs ) of major corporates and government agencies. These are busy people, but they are attracted by the idea of networking and mingling with their peers, as well as by the idea of hearing about a world they don't see too often (war zones) Usually they are 50+ years old, and are mostly men (but some women. They usually have pressing problems with the people around them, and want to help develop their teams.

Industry/Entity Type

Marketing

Requirements
Must have
• 1 page only
Nice to have
• something thought provoking or eye catching
Should not have
• any images with references to religion or violence

```html
<!DOCTYPE html>
<html lang="en">
<head>
<meta charset="utf-8">
<title>Conflict – Executive Invitation</title>
<link rel="stylesheet" href="https://fonts.googleapis.com/css2?family=Poppins:wght@500&family=Jost:wght@700&family=Libre+Bodoni:ital,wght@0,400;0,700;1,400&family=Arimo&display=swap">
<style>
  :root {
    --brand-red: #b3171f;
    --ink: #111111;
    --paper: #ffffff;
    --panel-dark: #000000;
    --photo-mid: #b9b6b2;
    --photo-dark: #6e6a66;
  }
  html, body {
    margin: 0;
    padding: 0;
    overflow: hidden;
    background: var(--paper);
  }
  .invitation {
    position: relative;
    width: 1200px;
    height: 848px;
    overflow: hidden;
    background: var(--paper);
  }
  .headline {
    position: absolute;
    left: 36px;
    top: 24px;
    width: 740px;
    height: 150px;
    margin: 0;
    font-size: 0;
    line-height: 0;
  }
  .headline svg { display: block; }
  .headline text {
    font-family: "Poppins", "Futura", sans-serif;
    font-weight: 500;
    font-size: 150px;
    fill: var(--brand-red);
  }
  .questions {
    position: absolute;
    left: 815px;
    top: 38px;
    margin: 0;
    padding: 0;
    list-style: none;
    font-family: "Jost", "Futura", sans-serif;
    font-weight: 700;
    font-size: 35px;
    line-height: 45px;
    letter-spacing: 1px;
    color: var(--ink);
  }
  .hero-photo {
    position: absolute;
    left: 0;
    top: 215px;
    width: 1200px;
    height: 365px;
    background:
      radial-gradient(ellipse 230px 170px at 440px 185px, var(--photo-dark), transparent 75%),
      radial-gradient(ellipse 230px 170px at 760px 185px, var(--photo-dark), transparent 75%),
      linear-gradient(180deg, var(--paper) 0%, var(--photo-mid) 30%, var(--photo-mid) 70%, var(--paper) 100%);
  }
  .photo-credit {
    position: absolute;
    left: 992px;
    top: 584px;
    font-family: "Arimo", "Arial", sans-serif;
    font-size: 7px;
    color: var(--ink);
  }
  .details-panel {
    position: absolute;
    left: 0;
    top: 622px;
    width: 800px;
    height: 226px;
    background: var(--brand-red);
    color: var(--paper);
    box-sizing: border-box;
    padding: 32px 40px 0 34px;
  }
  .lead {
    margin: 0;
    font-family: "Libre Bodoni", "Bodoni Moda", serif;
    font-style: italic;
    font-size: 17px;
    line-height: 20.5px;
  }
  .speaker-bio {
    margin: 8px 0 0;
    padding-right: 20px;
    font-family: "Arimo", "Arial", sans-serif;
    font-size: 10.6px;
    line-height: 12.5px;
  }
  .event-panel {
    position: absolute;
    left: 800px;
    top: 622px;
    width: 400px;
    height: 226px;
    background: var(--panel-dark);
    color: var(--paper);
    box-sizing: border-box;
    padding: 32px 42px 0 0;
    text-align: right;
    font-family: "Libre Bodoni", "Bodoni Moda", serif;
    font-weight: 700;
    font-size: 17px;
    line-height: 21px;
  }
  .event-panel p { margin: 0; }
  .sponsor { font-weight: 400; }
</style>
</head>
<body>
<main class="invitation">
  <h1 class="headline">
    <svg width="740" height="150" viewBox="0 0 740 150">
      <text x="0" y="131" textLength="730" lengthAdjust="spacingAndGlyphs">CONFLICT</text>
    </svg>
  </h1>
  <ul class="questions">
    <li>WITH THE BOARD?</li>
    <li>AT HOME?</li>
    <li>IN YOUR TEAM?</li>
  </ul>

  <div class="hero-photo" role="img" aria-label="Black and white photograph of two clenched fists meeting knuckle to knuckle"></div>
  <div class="photo-credit">Photograph © R. Ellis | Stockframe.com</div>

  <section class="details-panel">
    <p class="lead">Confict reduces effectiveness, creates political risk, and can destroy relationships. For inspiration on helping those around you manage conflict, come along to hear Dr Miles Harlan, entrepreneur, academic and “intercultural peacebuilder”. Miles has led conflict resolution projects around the world, from boardrooms and government agencies to Middle Eastern and Irish war zones. Join your peers for a fascinating insight into serious conflict and ways to build bridges that endure.</p>
    <p class="speaker-bio">Dr Harlan is Assistant Professor at Kealoha Pacific University, and was CEO of a successful internet startup sold to SportsWire in 2001. Currently, Dr Harlan is working on a project in the Middle East with the Calloway Institute and CourtBridge International to create sustainable peace among communities in Israel and the West Bank.</p>
  </section>

  <section class="event-panel">
    <p>Friday 13th August</p>
    <p>3pm start,</p>
    <p>4:30pm networking and nibbles.</p>
    <p>The Marrowgate Room, 48 Fenwick St.</p>
    <p>Entry $15; RSVP 04 555 0172</p>
    <p class="sponsor">Sponsored by Calloway Oceania</p>
    <p class="sponsor">www.callowayinstitute.com</p>
  </section>
</main>
</body>
</html>
```